Premium Food Label Design – High-End Boutique Jar Labels (3 Sizes)

I require a complete jar label redesign across three sizes:
75mm x 130mm (Large & Medium)
55mm x 120mm (Small)
45mm x 120mm (XS)

The design must feel professional, modern, elegant, and high-end boutique.
Primary aesthetic: white, minimal, refined, with accents in soft brown and gold/bronze. (see prefer colours of logo in OLD LABEL PDF)
Transparent background required.

I have attached my current label for wording reference only — I want to move away from the kraft look entirely.
The label must include all existing details, plus a dedicated space to manually add batch number and date.

IMPORTANT: Final files must be supplied as editable Adobe Illustrator (.AI) files with live text layers (not outlined) so I can update them as needed.
Logo is attached. I’m open to a fresh, elevated design direction aligned with a premium brand feel.
Updates

Low design quality

Target Market(s)

People who appreciate high-end, thoughtfully crafted food and are willing to pay for quality

Industry/Entity Type

Gourmet Food / Artisan Food Packaging

Requirements
Must have
• Premium, minimal aesthetic, Strong typography hierarchy, White background, Consistency across 3 sizes
Nice to have
• Elevated “Amber Meadow” styling
Should not have
• No bright or bold colours, No clutter or overcrowding, No heavy borders or thick frames,No “homemade/craft” fonts

```html
<!DOCTYPE html>
<html lang="en">
<head>
<meta charset="utf-8">
<title>Hearth Pantry – Tomato Relish Labels</title>
<link rel="stylesheet" href="https://fonts.googleapis.com/css2?family=Noto+Serif:wght@400;700&family=Noto+Serif+Display:wght@400&family=Dancing+Script:wght@500&family=Roboto+Condensed:wght@400&display=swap">
<style>
  :root {
    --backdrop: #e7e7e7;
    --label: #ffffff;
    --ink: #4a2219;
    --ink-soft: #5a3026;
  }
  * { margin: 0; padding: 0; box-sizing: border-box; }
  html, body { width: 1200px; height: 849px; overflow: hidden; }
  body {
    background: var(--backdrop);
    font-family: "Noto Serif", Georgia, serif;
    color: var(--ink);
    position: relative;
  }
  .label {
    position: absolute;
    top: 330px;
    width: 202px;
    height: 328px;
    background: var(--label);
    text-align: center;
  }
  .label--front { left: 217px; }
  .label--back { left: 817px; }
  .label > * { position: absolute; left: 0; right: 0; }

  /* Front */
  .brand-name {
    top: 388px; top: 60px;
    font-family: "Noto Serif", Georgia, serif;
    font-size: 15px;
    letter-spacing: 0.14em;
    color: var(--ink);
    display: flex; align-items: center; justify-content: center; gap: 6px;
  }
  .brand-name .dot {
    width: 6px; height: 6px; border-radius: 50%; background: var(--ink);
  }
  .product-name {
    top: 120px;
    font-family: "Noto Serif Display", "Noto Serif", serif;
    font-size: 29px;
    line-height: 27px;
    letter-spacing: 0.02em;
  }
  .product-variant {
    top: 190px;
    font-size: 9.5px;
    letter-spacing: 0.12em;
    color: var(--ink-soft);
  }
  .sign-off {
    top: 255px;
    font-family: "Dancing Script", cursive;
    font-size: 16px;
    color: var(--ink-soft);
  }
  .net-weight {
    top: 280px;
    font-size: 9.5px;
  }

  /* Back */
  .intention {
    top: 30px;
    font-weight: 700;
    font-size: 9.5px;
    line-height: 14px;
    letter-spacing: 0.06em;
  }
  .blessing {
    top: 79px;
    font-size: 10px;
    line-height: 14.5px;
    color: var(--ink-soft);
  }
  .ingredients {
    top: 146px;
    padding: 0 6px;
    font-size: 8px;
    line-height: 12px;
    color: var(--ink-soft);
  }
  .ingredients strong { letter-spacing: 0.04em; color: var(--ink); }
  .storage {
    top: 193px;
    font-family: "Roboto Condensed", "Arial Narrow", sans-serif;
    font-size: 7.2px;
    letter-spacing: 0.03em;
    color: var(--ink-soft);
    font-family: "Noto Serif", serif;
    transform: scaleX(0.86);
  }
  .batch-record {
    top: 225px;
    display: flex; justify-content: center; gap: 28px;
    font-size: 7.5px;
    color: var(--ink-soft);
  }
  .maker { top: 244px; font-size: 8px; line-height: 11px; }
  .maker strong { display: block; font-size: 8.5px; }
  .contact { top: 268px; font-size: 7.5px; line-height: 11px; color: var(--ink-soft); }
</style>
</head>
<body>
  <section class="label label--front" aria-label="Front label">
    <div class="brand-name"><span class="dot"></span>HEARTH PANTRY</div>
    <h1 class="product-name">TOMATO<br>RELISH</h1>
    <p class="product-variant">POPULAR CHOICE</p>
    <p class="sign-off">Made with love</p>
    <p class="net-weight">375g</p>
  </section>

  <section class="label label--back" aria-label="Back label">
    <h2 class="intention">AMBER MEADOW<br>WHAT IS MADE WITH LOVE<br>IS FELT IN RETURN.</h2>
    <p class="blessing">May this relish nourish more<br>than the meal- bringing comfort,<br>connection , and joy to<br>every moment shared.</p>
    <p class="ingredients"><strong>INGREDIENTS:</strong> Tomatoes, onion, sugar,<br>vinegar, salt, spices, thickener (cornflour)</p>
    <p class="storage">STORAGE: KEEP REFRIGERATED ONCE OPENED</p>
    <div class="batch-record"><span>Batch #</span><span>Date:</span></div>
    <p class="maker"><strong>Made by Hearth Pantry</strong>QLD, Australia</p>
    <p class="contact">info@hearthpantry.com<br>www.hearthpantry.com</p>
  </section>
</body>
</html>
```